Love Your Hearing - Life Sounds Good

I need a website. I had a company doing it, and it looked very nice, but they went way up on hosting costs and said they owned the design of the site. I changed hosts to keep costs down. You can see the current design at crestvaleaudio.com. They said I could use the copy and images from the current website. So you could cut and paste to speed things up. My logo and other images are on the current website. If you are unable to use I can send other digital copies.

Target Market(s)

seniors 55 and up

Number of Pages Required

4 page

Font styles to use
Sans Serif

Colors
0255a3
f78f20

Requirements
Must have
• Video testimonies that I can add without assistance. I use youtube links for the videos.
Nice to have
• The color scheme theme can be drawn from the logo, which is on the current webstie crestvaleaudio.com
Should not have
• Should not have anything related to SonoPath on the website.

```html
<!DOCTYPE html>
<html lang="en">
<head>
<meta charset="utf-8">
<title>Crestvale Hearing Center</title>
<link href="https://fonts.googleapis.com/css2?family=Roboto+Slab:wght@300;400;500;700&family=Poppins:wght@300;400;500;600;700&display=swap" rel="stylesheet">
<style>
:root{
  --blue:#0255a3;
  --orange:#f78f20;
  --orange-deep:#ee7414;
  --ink:#222;
  --text:#333;
  --darker:#1f1f1f;
  --white:#fff;
  --line:#bbb;
  --font-head:"Roboto Slab","Poppins",sans-serif;
  --font-body:"Poppins",sans-serif;
}
*{margin:0;padding:0;box-sizing:border-box}
html,body{width:1200px;height:5072px;overflow:hidden;background:var(--white)}
body{position:relative;font-family:var(--font-head);color:var(--text)}
.abs{position:absolute}
.btn{position:absolute;background:var(--orange);color:var(--white);border-radius:28px;font-family:var(--font-head);font-weight:500;display:flex;align-items:center;justify-content:center;gap:8px;box-shadow:0 3px 8px rgba(0,0,0,.15)}
.btn svg{width:16px;height:16px}

/* header */
.site-header{position:absolute;left:0;top:0;width:1200px;height:148px;background:var(--white);box-shadow:0 2px 6px rgba(0,0,0,.15);z-index:5}
.brand{position:absolute;display:flex;align-items:center;gap:10px}
.brand-mark{width:44px;height:44px;background:var(--orange)}
.brand-name{font-family:var(--font-head);font-weight:700;color:var(--blue);font-size:36px;line-height:1;letter-spacing:1px}
.support{left:598px;top:22px;display:flex;gap:10px;align-items:center}
.support-label{color:var(--blue);font-weight:700;font-size:16px;font-family:var(--font-body)}
.support-num{font-size:16px;color:#222;font-family:var(--font-body)}
.search{left:875px;top:28px;width:235px;height:42px;border:1px solid #ddd;border-radius:21px;font-size:13px;color:#999;padding:11px 20px;font-family:var(--font-body)}
.search-btn{position:absolute;right:4px;top:5px;width:30px;height:30px;border-radius:50%;background:var(--orange)}
.nav{left:488px;top:102px;display:flex;gap:31px;font-size:17px;color:#333;font-family:var(--font-head)}

/* hero */
.hero-photo{left:0;top:148px;width:1200px;height:720px;background:
  radial-gradient(ellipse 28% 22% at 27% 72%,rgba(176,52,36,.85),transparent 70%),
  radial-gradient(ellipse 24% 14% at 92% 72%,rgba(170,56,38,.8),transparent 70%),
  radial-gradient(ellipse 30% 40% at 22% 40%,rgba(120,80,60,.55),transparent 70%),
  radial-gradient(ellipse 40% 18% at 62% 48%,rgba(255,236,200,.75),transparent 70%),
  linear-gradient(180deg,#d8d4cb 0%,#a9a293 12%,#3d4a3b 26%,#56624f 36%,#b3ad9c 46%,#8e8170 56%,#6b4a36 70%,#4e3626 85%,#2f2219 100%)}
.hero-brand{left:595px;top:280px}
.hero-title{left:595px;top:372px;font-size:37px;font-weight:700;color:var(--white);text-shadow:0 1px 4px rgba(0,0,0,.35)}
.hero-sub{left:595px;top:432px;font-size:27px;color:var(--white);font-weight:400;text-shadow:0 1px 4px rgba(0,0,0,.35)}

/* welcome */
.welcome-kicker{left:0;width:1200px;top:900px;text-align:center;font-size:34px;font-weight:500;color:var(--ink)}
.welcome-title{left:0;width:1200px;top:948px;text-align:center;font-size:46px;font-weight:500;color:var(--blue)}
.welcome-title span{color:var(--orange)}
.rule{left:380px;top:1033px;width:440px;height:1px;background:var(--line)}
.rule-mark{left:565px;top:1030px;width:70px;height:6px;background:var(--blue)}
.welcome-copy{left:130px;width:940px;top:1063px;text-align:center;font-size:17px;line-height:40px;color:#333}

.spec-photo{left:85px;top:1215px;width:340px;height:340px;border-radius:50%;border:5px solid var(--orange);border-top-color:var(--blue);border-right-color:var(--blue);padding:8px}
.spec-photo div{width:100%;height:100%;border-radius:50%;background:
  radial-gradient(ellipse 50% 30% at 50% 100%,#f2f4f6 0%,#dfe3e8 60%,transparent 62%),
  radial-gradient(ellipse 10% 22% at 52% 88%,#2a4a8a,transparent 70%),
  radial-gradient(circle at 50% 40%,#e4b9a0 0%,#d6a48a 18%,transparent 30%),
  linear-gradient(180deg,#e9e9e9,#cfd3d7)}
.spec-title{left:468px;top:1236px;font-size:27px;color:var(--blue);font-weight:400}
.spec-copy{left:468px;width:640px;top:1284px;font-size:15px;line-height:34px;text-align:justify;color:#222}

/* services */
.svc-photo{left:0;top:1650px;width:1200px;height:720px;background:
  radial-gradient(ellipse 22% 30% at 48% 28%,rgba(205,185,160,.55),transparent 70%),
  radial-gradient(ellipse 28% 40% at 85% 55%,rgba(160,120,90,.55),transparent 70%),
  radial-gradient(ellipse 25% 35% at 20% 35%,rgba(120,110,100,.5),transparent 70%),
  linear-gradient(120deg,#2b2b2b 0%,#3e3b38 45%,#5b4c40 75%,#7a5d44 100%)}
.svc-title{left:90px;top:1782px;font-size:36px;color:var(--white);font-weight:500}
.svc-list{left:90px;top:1858px;width:262px;background:var(--white);list-style:none}
.svc-list li{height:53px;line-height:53px;padding-left:22px;font-size:15px;color:#333;border-bottom:1px solid #ddd}
.svc-list li.active{background:var(--orange);color:var(--white)}
.svc-circle{left:375px;top:1905px;width:280px;height:280px;border-radius:50%;border:4px solid var(--orange);background:
  radial-gradient(ellipse 16% 38% at 58% 62%,#e8b898,transparent 70%),
  radial-gradient(circle at 40% 45%,#cfd3d8 0%,transparent 12%),
  radial-gradient(circle,#ffffff,#e6e6e6)}
.svc-heading{left:675px;top:1898px;font-size:24px;color:var(--white);font-weight:500}
.svc-copy{left:675px;width:433px;top:1942px;font-size:15px;line-height:36px;color:#ddd;text-align:justify}

/* aids */
.aids-title{left:90px;top:2490px;font-size:34px;line-height:48px;color:var(--blue);font-weight:700}
.aids-copy{left:90px;width:540px;top:2596px;font-size:15.5px;line-height:36px;color:#222;text-align:justify}
.aids-ring{left:668px;top:2465px;width:450px;height:450px;border-radius:50%;border:4px solid var(--orange);background:var(--white);box-shadow:0 0 12px rgba(0,0,0,.12)}
.aids-img{left:695px;top:2492px;width:396px;height:396px;border-radius:50%;background:
  radial-gradient(ellipse 12% 20% at 50% 50%,#b8c65a,transparent 75%),
  radial-gradient(ellipse 8% 10% at 70% 62%,#2a2a2a,transparent 75%),
  radial-gradient(ellipse 7% 9% at 84% 56%,#9b5a3c,transparent 75%),
  radial-gradient(ellipse 8% 9% at 22% 65%,#e8d0d4,transparent 75%),
  radial-gradient(circle,#ffffff,#f5f5f2)}

/* testimonials */
.testi-photo{left:0;top:3010px;width:1200px;height:720px;background:
  radial-gradient(ellipse 22% 30% at 30% 20%,rgba(150,130,105,.55),transparent 70%),
  radial-gradient(ellipse 18% 35% at 12% 55%,rgba(130,125,115,.45),transparent 70%),
  radial-gradient(ellipse 20% 32% at 55% 28%,rgba(95,80,70,.6),transparent 70%),
  radial-gradient(ellipse 25% 40% at 85% 50%,rgba(90,70,50,.55),transparent 70%),
  linear-gradient(100deg,#3a3836 0%,#282625 50%,#3b3129 100%)}
.testi-title{left:0;width:1200px;top:3200px;text-align:center;font-size:46px;color:var(--white);font-weight:500}
.testi-quote{left:180px;width:840px;top:3418px;text-align:justify;text-align-last:center;font-size:18px;line-height:36px;color:#eee}
.testi-name{left:0;width:1200px;top:3550px;text-align:center;font-size:18px;color:var(--white);font-weight:700;font-family:var(--font-body)}

/* news */
.news-title{left:0;width:1200px;top:3810px;text-align:center;font-size:36px;color:var(--blue);font-weight:700}
.card{position:absolute;top:3905px;width:330px}
.card-img{width:330px;height:195px}
.card-date{position:absolute;left:25px;top:182px;background:var(--orange);color:var(--white);font-size:13px;padding:5px 12px;font-family:var(--font-body)}
.card h3{margin-top:50px;font-size:15px;line-height:26px;color:var(--blue);font-weight:400;text-transform:uppercase}
.card p{margin-top:6px;font-size:11.5px;line-height:25px;color:#333;font-family:var(--font-body)}
.card .more{margin-top:10px;font-size:12px;color:var(--orange);font-family:var(--font-body);font-weight:600}

/* footer */
.footer{left:0;top:4560px;width:1200px;height:512px;background:var(--darker)}
.f-head{font-size:22px;color:var(--white);font-weight:400}
.f-text{font-size:13px;color:#ddd;line-height:22px}
.f-links{list-style:none}
.f-links li{font-size:13px;color:#ddd;line-height:27px;display:flex;align-items:center;gap:12px}
.f-links li::before{content:"";width:8px;height:8px;border-radius:50%;background:#ddd}
.social{display:flex;gap:6px}
.social span{width:26px;height:26px;border-radius:50%;border:1.5px solid #ddd}
.newsletter-input{width:288px;height:44px;background:var(--white);font-size:11px;color:#777;padding:14px;font-family:var(--font-body)}
.newsletter-btn{border:2px solid #ddd;color:var(--white);font-size:12px;font-weight:700;padding:10px 12px;font-family:var(--font-body)}
.copyright{left:0;width:1200px;top:5002px;text-align:center;font-size:13px;color:#ddd;font-family:var(--font-body)}
</style>
</head>
<body>

<header class="site-header">
  <div class="brand" style="left:90px;top:46px"><span class="brand-mark"></span><span class="brand-name">CRESTVALE</span></div>
  <div class="abs support">
    <svg width="38" height="38" viewBox="0 0 38 38"><circle cx="19" cy="19" r="17" fill="none" stroke="#f78f20" stroke-width="3"/><path d="M13 11c2 0 3 4 2 5l-1 1c1 3 3 5 6 6l1-1c1-1 5 0 5 2l-1 3c-7 0-13-6-13-13z" fill="#f78f20"/></svg>
    <div><div class="support-label">SUPPORT CALL US</div><div class="support-num">(555) 214-3380</div></div>
  </div>
  <div class="abs search">Search<span class="search-btn"></span></div>
  <nav class="abs nav"><span>Home</span><span>Hearing Aids</span><span>Services</span><span>Education</span><span>About Us</span><span>Contact</span></nav>
</header>

<section>
  <div class="abs hero-photo" role="img" aria-label="Couple with kayaks on a lakeshore at sunset"></div>
  <div class="brand hero-brand"><span class="brand-mark" style="background:#fff"></span><span class="brand-name" style="color:#fff">CRESTVALE</span></div>
  <h1 class="abs hero-title">Recapture the sounds of life</h1>
  <p class="abs hero-sub">and the intimacy of a quiet conversation</p>
  <div class="btn" style="left:595px;top:488px;width:240px;height:48px;font-size:16px;font-weight:400">Take Action Today <svg viewBox="0 0 16 16"><circle cx="8" cy="8" r="7" fill="#fff"/><path d="M6 4l4 4-4 4z" fill="#f78f20"/></svg></div>
  <svg class="abs" style="left:0;top:660px" width="1200" height="210" viewBox="0 0 1200 210">
    <path d="M0 120 C250 50 500 140 760 40 C950 -20 1100 40 1200 90 L1200 210 L0 210 Z" fill="#fff"/>
    <path d="M0 120 C250 40 500 120 760 30 C950 -25 1100 30 1200 80 L1200 120 C1100 60 950 10 760 60 C500 150 250 70 0 130 Z" fill="#f78f20"/>
    <path d="M700 60 C900 -10 1080 40 1200 120 L1200 200 C1100 110 950 40 760 62 Z" fill="#ee7414"/>
  </svg>
</section>

<section>
  <h2 class="abs welcome-kicker">Welcome to</h2>
  <h2 class="abs welcome-title">Crestvale <span>Hearing Center LLC</span></h2>
  <div class="abs rule"></div><div class="abs rule-mark"></div>
  <p class="abs welcome-copy">We provide hearing evaluations, counseling, and fitting of hearing aids. We service all the major brands of hearing aids including Aurivo, Sonawave, Kellmark, Vistone, Lumaphon, Brightear, Nanotone, Clarivo, Audena, Harlow, Quietline, and others.</p>
  <div class="abs spec-photo"><div role="img" aria-label="Portrait of the hearing specialist in a white coat"></div></div>
  <h3 class="abs spec-title">Meet the Specialist, Daniel Whitford</h3>
  <p class="abs spec-copy">I was first introduced to hearing aids as a patient. At the tender age of 36, I was diagnosed with profound hearing loss by a hearing healthcare provider in Fairhaven, North Carolina. I was fitted with two in-the-ear hearing aids that instantly changed my life! There was no more straining to hear what people were saying, and no more trying to piece together a discussion to make sense of the conversation.</p>
  <div class="btn" style="left:468px;top:1470px;width:207px;height:54px;font-size:16px">READ MORE <svg viewBox="0 0 16 16"><circle cx="8" cy="8" r="7" fill="#fff"/><path d="M6 4l4 4-4 4z" fill="#f78f20"/></svg></div>
</section>

<section>
  <div class="abs svc-photo" role="img" aria-label="Smiling senior couple outdoors at golden hour"></div>
  <svg class="abs" style="left:0;top:1640px" width="1200" height="80" viewBox="0 0 1200 80"><path d="M0 0 H1200 V40 C900 -10 600 60 0 20 Z" fill="#fff"/><path d="M0 20 C500 50 800 5 1200 40 L1200 46 C800 15 500 60 0 30 Z" fill="#0255a3"/></svg>
  <h2 class="abs svc-title">Our Services</h2>
  <ul class="abs svc-list">
    <li>Hearing Evaluations</li><li>Video Otoscopy</li><li class="active">Hearing Aid Fitting</li><li>Follow Up Service</li><li>Ear Molds</li><li>Wireless Technology</li><li>Tinnitus Treatment</li>
  </ul>
  <div class="abs svc-circle" role="img" aria-label="Hand holding a small hearing aid"></div>
  <h3 class="abs svc-heading">HEARING AID FITTING</h3>
  <p class="abs svc-copy">The first fit is established for the patient using information from the audiogram and the software provided by the manufacturer. Thereafter, adjustments will be made to maximize the comfort, sound quality, and performance of the hearing aid.</p>
  <div class="btn" style="left:675px;top:2132px;width:177px;height:48px;font-size:15px;font-weight:400">READ MORE <svg viewBox="0 0 16 16"><circle cx="8" cy="8" r="7" fill="#fff"/><path d="M6 4l4 4-4 4z" fill="#f78f20"/></svg></div>
  <svg class="abs" style="left:0;top:2270px" width="1200" height="110" viewBox="0 0 1200 110"><path d="M0 70 C300 0 600 40 900 40 C1050 40 1150 60 1200 60 L1200 110 L0 110 Z" fill="#fff"/><path d="M700 40 C900 30 1100 50 1200 55 L1200 90 C1100 70 900 40 700 42 Z" fill="#f78f20"/></svg>
</section>

<section>
  <h2 class="abs aids-title">HEARING AIDS AT CRESTVALE<br>HEARING CENTER</h2>
  <p class="abs aids-copy">For most people, hearing loss takes place gradually. Unconsciously, they develop strategies to help them cope better with daily interactions with people, like reading lips, guessing contextually, filling in the blanks, and smiling and faking it. At some point the frustration is overwhelming, and it's obvious that something is not right with their hearing and action needs to be taken.</p>
  <div class="btn" style="left:88px;top:2835px;width:177px;height:48px;font-size:15px;font-weight:400">READ MORE <svg viewBox="0 0 16 16"><circle cx="8" cy="8" r="7" fill="#fff"/><path d="M6 4l4 4-4 4z" fill="#f78f20"/></svg></div>
  <div class="abs aids-ring"></div>
  <div class="abs aids-img" role="img" aria-label="Assorted hearing aid models in green, black and bronze"></div>
</section>

<section>
  <div class="abs testi-photo" role="img" aria-label="Patient speaking in a clinic office, video still"></div>
  <svg class="abs" style="left:0;top:3000px" width="1200" height="90" viewBox="0 0 1200 90"><path d="M0 0 H1200 V60 C900 90 500 -10 0 30 Z" fill="#fff"/><path d="M0 30 C300 10 500 20 700 40 L700 46 C500 26 300 18 0 40 Z" fill="#f78f20"/></svg>
  <h2 class="abs testi-title">Testimonials</h2>
  <svg class="abs" style="left:572px;top:3300px" width="56" height="40" viewBox="0 0 56 40"><path d="M0 40V22C0 8 8 2 20 0v8c-6 2-9 6-9 12h9v20zM30 40V22C30 8 38 2 50 0v8c-6 2-9 6-9 12h9v20z" fill="#ddd"/></svg>
  <svg class="abs" style="left:574px;top:3360px" width="52" height="52" viewBox="0 0 52 52"><circle cx="26" cy="26" r="24" fill="none" stroke="#ddd" stroke-width="2"/><path d="M21 16l14 10-14 10z" fill="none" stroke="#ddd" stroke-width="2"/></svg>
  <svg class="abs" style="left:66px;top:3350px" width="70" height="40" viewBox="0 0 70 40"><path d="M68 20H4M22 2L3 20l19 18" fill="none" stroke="#fff" stroke-width="3"/></svg>
  <svg class="abs" style="left:1065px;top:3350px" width="70" height="40" viewBox="0 0 70 40"><path d="M2 20h64M48 2l19 18-19 18" fill="none" stroke="#fff" stroke-width="3"/></svg>
  <p class="abs testi-quote">“ Sed ut perspiciatis unde omnis iste natus error sit voluptatem accusantium doloremque laudantium, totam rem aperiam, eaque ipsa quae ab illo inventore veritatis et quasi architecto beatae vitae dicta sunt explicabo. ”</p>
  <p class="abs testi-name">Walter (06/09/2013)</p>
  <svg class="abs" style="left:0;top:3630px" width="1200" height="110" viewBox="0 0 1200 110"><path d="M0 70 C400 110 800 40 1200 80 L1200 110 L0 110 Z" fill="#fff"/><path d="M500 80 C800 60 1000 60 1200 70 L1200 90 C1000 75 800 75 500 82 Z" fill="#f78f20"/></svg>
</section>

<section>
  <h2 class="abs news-title">NEWS &amp; EVENTS</h2>
  <article class="card" style="left:88px">
    <div class="card-img" role="img" aria-label="Aerial view of a river and forest at dusk" style="background:radial-gradient(ellipse 40% 20% at 50% 60%,#b7c2c8,transparent 70%),linear-gradient(180deg,#e0b887 0%,#c79a72 25%,#5f6f58 45%,#8e9ea6 62%,#3c5540 80%,#2f4634 100%)"></div>
    <span class="card-date">Dec 19 2018</span>
    <h3>Do's and don'ts for communicating during the holidays</h3>
    <p>Sed ut perspiciatis unde omnis iste natus error sit voluptatem accusantium doloremque laudantium, totam rem aperiam, eaque ipsa quae ab illo</p>
    <div class="more">READ MORE</div>
  </article>
  <article class="card" style="left:435px">
    <div class="card-img" role="img" aria-label="Joyful senior woman with arms raised outdoors" style="background:radial-gradient(ellipse 18% 45% at 50% 70%,#6a7a86,transparent 75%),radial-gradient(ellipse 60% 30% at 50% 10%,#f5f5f3,transparent 70%),linear-gradient(180deg,#dcdfe0 0%,#a7aeb2 50%,#5f676d 100%)"></div>
    <span class="card-date">Jun 01 2018</span>
    <h3>Communication for all: how people of all ages benefit</h3>
    <p>Sed ut perspiciatis unde omnis iste natus error sit voluptatem accusantium doloremque laudantium, totam rem aperiam, eaque ipsa quae ab illo</p>
    <div class="more">READ MORE</div>
  </article>
  <article class="card" style="left:782px">
    <div class="card-img" role="img" aria-label="Card payment terminal on a counter" style="background:radial-gradient(ellipse 30% 40% at 80% 30%,#e9a24a,transparent 70%),radial-gradient(ellipse 22% 35% at 22% 45%,#2a2a2a,transparent 75%),linear-gradient(135deg,#1c130e 0%,#4e2d18 50%,#b06a2c 100%)"></div>
    <span class="card-date">Sep 14 2018</span>
    <h3>Over-the-counter hearing aids: what you need to know</h3>
    <p>Sed ut perspiciatis unde omnis iste natus error sit voluptatem accusantium doloremque laudantium, totam rem aperiam, eaque ipsa quae ab illo</p>
    <div class="more">READ MORE</div>
  </article>
</section>

<footer>
  <div class="abs footer"></div>
  <svg class="abs" style="left:0;top:4350px" width="1200" height="260" viewBox="0 0 1200 260">
    <path d="M0 100 C250 220 600 240 1200 180 L1200 260 L0 260 Z" fill="#1f1f1f"/>
    <path d="M0 0 C50 120 250 190 600 200 C850 205 1050 170 1200 150 L1200 175 C1050 200 850 225 600 220 C250 210 60 150 0 60 Z" fill="#f78f20"/>
    <path d="M0 60 C80 150 300 200 600 200 C300 215 80 180 0 110 Z" fill="#ee7414"/>
    <path d="M300 210 C600 240 900 210 1200 165 L1200 172 C900 222 600 250 300 212 Z" fill="#0255a3"/>
  </svg>
  <div class="brand" style="left:110px;top:4770px;gap:8px"><span class="brand-mark" style="width:26px;height:26px;background:#fff"></span><span class="brand-name" style="color:#fff;font-size:19px">CRESTVALE</span></div>
  <div class="abs social" style="left:125px;top:4818px"><span></span><span></span><span></span><span></span></div>

  <h4 class="abs f-head" style="left:330px;top:4706px">CONTACT US</h4>
  <svg class="abs" style="left:332px;top:4762px" width="16" height="20" viewBox="0 0 16 20"><path d="M8 1a6 6 0 0 1 6 6c0 5-6 12-6 12S2 12 2 7a6 6 0 0 1 6-6z" fill="none" stroke="#ddd" stroke-width="1.5"/><circle cx="8" cy="7" r="2" fill="#ddd"/></svg>
  <p class="abs f-text" style="left:367px;top:4758px">240 Elm Ridge Rd, Suite 12,<br>Crestvale, NC 28000</p>
  <svg class="abs" style="left:332px;top:4810px" width="16" height="16" viewBox="0 0 16 16"><path d="M3 1c2 0 3 3 2 4l-1 1c1 2 3 4 5 5l1-1c1-1 4 0 4 2l-1 3C7 15 1 9 1 3z" fill="none" stroke="#ddd" stroke-width="1.3"/></svg>
  <p class="abs f-text" style="left:367px;top:4808px">Phone : (555) 214-3380</p>
  <svg class="abs" style="left:332px;top:4848px" width="18" height="13" viewBox="0 0 18 13"><rect x="1" y="1" width="16" height="11" fill="none" stroke="#ddd" stroke-width="1.3"/><path d="M1 1l8 6 8-6" fill="none" stroke="#ddd" stroke-width="1.3"/></svg>
  <p class="abs f-text" style="left:367px;top:4844px">Email:<br>info@crestvaleaudio.com</p>

  <h4 class="abs f-head" style="left:587px;top:4706px">QUICK LINKS</h4>
  <ul class="abs f-links" style="left:588px;top:4755px"><li>Home</li><li>Hearing Aids</li><li>Services</li><li>Education</li><li>About Us</li><li>Contact</li></ul>

  <h4 class="abs f-head" style="left:780px;top:4706px">SIGN UP FOR NEWSLETTER</h4>
  <p class="abs f-text" style="left:781px;top:4752px;width:300px;font-size:12px;line-height:25px">Excepteur sint occaecat cupidatat non proident, sunt in culpa qui officia deserunt</p>
  <div class="abs newsletter-input" style="left:780px;top:4815px">Enter email</div>
  <div class="abs newsletter-btn" style="left:780px;top:4880px">SUBSCRIPTION</div>

  <div class="abs" style="left:80px;top:4985px;width:1040px;height:1px;background:#444"></div>
  <p class="abs copyright">2019 © Copyrights. All Rights Reserved</p>
</footer>

</body>
</html>
```